Storage Auctions Book Cover

I need a new cover for my book which is located here:
http://www.quillmart-example.com/dp/R417TZ2WQX/
The book is about making money by buying storage units at auction, made popular by the reality shows "Locker Clash" and "Gavel Trackers." It's for entrepreneurs and those looking for a weekend business.
The current cover was homemade in Gimp, and it's holding back sales. I think it needs a better cover in order to look more professional and catch more attention.
Updates
So far, I really like the designs from Pimbleworth and vostacraft. Consider those two what I'm looking for, they are both good.
Industry/Entity Type
Storage
Look and feel
Each slider illustrates characteristics of the customer's brand and the style your logo design should communicate.

```html
<!DOCTYPE html>
<html lang="en">
<head>
<meta charset="utf-8">
<title>Making Money in Storage Auctions – Book Cover</title>
<link rel="stylesheet" href="https://fonts.googleapis.com/css2?family=Arimo:wght@700&family=Allura&display=swap">
<style>
  :root {
    --cover-red: #d8261c;
    --cover-red-dark: #a9130d;
    --title-cream: #fff7c4;
    --title-shadow: #7a0c07;
    --band-yellow: #f7ec9a;
    --door-white: #fbfbfd;
    --door-blue: #d9dfee;
    --door-line: #a9adb6;
    --ink-black: #141414;
    --script-red: #c8262a;
    --byline-yellow: #fbe97f;
  }
  html, body {
    margin: 0;
    padding: 0;
    overflow: hidden;
    background: #ffffff;
  }
  .cover {
    position: relative;
    width: 801px;
    height: 1200px;
    overflow: hidden;
    background: radial-gradient(ellipse at 50% 45%, var(--cover-red) 55%, var(--cover-red-dark) 100%);
    font-family: "Arimo", Arial, sans-serif;
  }
  .headline {
    position: absolute;
    left: 0;
    width: 100%;
    margin: 0;
    text-align: center;
    font-weight: 700;
    font-size: 168px;
    line-height: 1;
    color: var(--title-cream);
    letter-spacing: 1px;
    text-shadow: 5px 6px 2px var(--title-shadow);
  }
  .headline--making { top: 8px; }
  .headline--money { top: 186px; }
  .band {
    position: absolute;
    left: 0;
    width: 100%;
    height: 11px;
    background: var(--band-yellow);
  }
  .band--top { top: 376px; }
  .band--bottom { top: 1010px; }
  .door {
    position: absolute;
    left: 0;
    top: 387px;
    width: 100%;
    height: 623px;
    background:
      repeating-linear-gradient(to bottom, transparent 0 27px, var(--door-line) 27px 29px),
      linear-gradient(to bottom, var(--door-blue) 0%, var(--door-white) 10%, var(--door-white) 88%, var(--door-blue) 100%);
  }
  .subject {
    position: absolute;
    left: 0;
    width: 100%;
    margin: 0;
    text-align: center;
    font-weight: 700;
    color: var(--ink-black);
    line-height: 1;
  }
  .subject--in-storage { top: 415px; font-size: 92px; }
  .subject--auctions { top: 512px; font-size: 110px; }
  .tagline {
    position: absolute;
    left: 0;
    top: 700px;
    width: 100%;
    margin: 0;
    text-align: center;
    font-family: "Allura", cursive;
    font-size: 62px;
    line-height: 54px;
    color: var(--script-red);
  }
  .byline {
    position: absolute;
    left: 0;
    top: 1115px;
    width: 100%;
    margin: 0;
    text-align: center;
    font-weight: 700;
    font-size: 34px;
    color: var(--byline-yellow);
  }
</style>
</head>
<body>
  <main class="cover">
    <h1 class="headline headline--making">MAKING</h1>
    <p class="headline headline--money">MONEY</p>
    <div class="band band--top"></div>
    <div class="door"></div>
    <p class="subject subject--in-storage">IN STORAGE</p>
    <p class="subject subject--auctions">AUCTIONS</p>
    <p class="tagline">How to Profit from the<br>Locker Clash and become a<br>Storage Auction Warrior</p>
    <div class="band band--bottom"></div>
    <p class="byline">By Dalton Pryce</p>
  </main>
</body>
</html>
```